BRISKLE sparkling water needs new artwork! Based in Southern California

"Briskle" is a new sparkling water company based in Southern California that offers refreshing flavors (lime, cherry, & mango) with B vitamins and antioxidants.

We would like to see packaging designs for standard 12oz cans for each of the three flavors.
Our initial preference is to have individual artwork for each flavor.

Attached are examples of competitors' designs.
Updates

We are extending the deadline for the Thanksgiving Holiday. Thank you all for your contributions.

```html
<!DOCTYPE html>
<html lang="en">
<head>
<meta charset="utf-8">
<title>Briskle Cherry Sparkling Water – 109 mm Can Label Template</title>
<link rel="stylesheet" href="https://fonts.googleapis.com/css2?family=Baloo+2:wght@800&family=Kalam:wght@700&family=Source+Sans+3:wght@400;700&display=swap">
<style>
  :root {
    --label-pink: #f5607a;
    --guide-lilac: #a98bc9;
    --bubble-blue: #4a5cc8;
    --accent-red: #e0203a;
    --ink: #1c1c1c;
    --paper: #ffffff;
    --cherry-red: #e24a5c;
    --sketch-pink: #f06f86;
    --wave-white: #fbe9ed;
  }
  * { margin: 0; padding: 0; box-sizing: border-box; }
  html, body { width: 1200px; height: 714px; overflow: hidden; background: var(--paper); }
  .template { position: relative; width: 1200px; height: 714px; font-family: "Source Sans 3", Arial, sans-serif; }
  .template svg { position: absolute; inset: 0; }

  .guide-text { fill: var(--guide-lilac); font-family: "Source Sans 3", Arial, sans-serif; }
  .template-title { font-size: 22px; }
  .guide-label { font-size: 11px; }
  .guide-label-sm { font-size: 9px; }
  .guide-label-md { font-size: 13px; }
  .guide-strong { font-weight: 700; font-size: 13px; }
  .guide-line { stroke: var(--guide-lilac); stroke-width: 1; fill: none; }
  .guide-dash { stroke: var(--guide-lilac); stroke-width: 1.3; stroke-dasharray: 10 8; }

  .label-field { fill: var(--label-pink); }
  .brand-name { font-family: "Baloo 2", "Arial Rounded MT Bold", sans-serif; font-weight: 800; fill: var(--ink); }
  .callout-bubble { fill: var(--bubble-blue); stroke: var(--ink); stroke-width: 1.2; }
  .callout-text { font-family: "Kalam", "Comic Sans MS", cursive; font-weight: 700; fill: var(--paper); }
  .callout-accent { fill: var(--accent-red); }
  .headline-panel { fill: var(--paper); stroke: var(--ink); stroke-width: 2; }
  .headline-text { font-family: "Kalam", "Comic Sans MS", cursive; font-weight: 700; fill: var(--ink); }
  .ribbon { fill: var(--bubble-blue); stroke: var(--ink); stroke-width: 1; }
  .stat-badge { fill: var(--label-pink); stroke: var(--bubble-blue); stroke-width: 2.5; }
  .stat-number { font-family: "Kalam", cursive; font-weight: 700; fill: var(--paper); font-size: 18px; }
  .stat-word { font-family: "Kalam", cursive; font-weight: 700; fill: var(--paper); font-size: 4px; }
  .volume { font-family: "Kalam", cursive; font-weight: 700; fill: var(--paper); font-size: 13px; }
  .placeholder-box { fill: var(--paper); }
  .placeholder-text { font-family: "Source Sans 3", Arial, sans-serif; font-size: 13px; fill: #000; }
</style>
</head>
<body>
<main class="template">
<svg width="1200" height="714" viewBox="0 0 1200 714" xmlns="http://www.w3.org/2000/svg">

  <text class="guide-text template-title" x="600" y="21" text-anchor="middle">109 mm LF_4.875”_Template</text>

  <!-- label background -->
  <rect class="label-field" x="146" y="133" width="874" height="493"/>

  <!-- illustration zones -->
  <rect x="392" y="228" width="100" height="150" rx="30" fill="var(--sketch-pink)" role="img" aria-label="Line-drawn cherries with leaves, left of headline"/>
  <rect x="690" y="240" width="100" height="150" rx="30" fill="var(--sketch-pink)" role="img" aria-label="Line-drawn cherries with leaves, right of headline"/>
  <rect x="411" y="385" width="373" height="62" rx="28" fill="var(--wave-white)" role="img" aria-label="White curling waves splashing either side of the headline"/>
  <rect x="450" y="463" width="124" height="154" rx="40" fill="var(--cherry-red)" role="img" aria-label="Pair of red cherries on a stem with a green leaf"/>

  <!-- back panel -->
  <text class="brand-name" x="262" y="252" font-size="36" text-anchor="middle">briskle</text>

  <path class="callout-bubble" d="M180 300 Q200 272 270 276 Q340 282 348 318 Q350 352 306 360 L300 374 L288 364 Q230 372 192 354 Q168 330 180 300 Z"/>
  <text class="callout-text" font-size="14" x="194" y="305">YOUR</text>
  <text class="callout-text callout-accent" font-size="22" x="266" y="326" text-anchor="middle">BRISKLE</text>
  <text class="callout-text" font-size="14" x="262" y="346" text-anchor="middle">SODA ALTERNATIVE</text>

  <path class="callout-bubble" d="M222 410 Q230 390 268 392 Q314 396 316 432 Q316 466 290 474 L300 486 L276 476 Q232 478 222 452 Z"/>
  <text class="callout-text" font-size="17" x="268" y="418" text-anchor="middle">THE B´S</text>
  <text class="callout-text" font-size="17" x="268" y="440" text-anchor="middle">HELP:</text>
  <text class="callout-text" font-size="13" x="268" y="462" text-anchor="middle">B6 &amp; B12</text>

  <rect class="callout-bubble" x="234" y="485" width="66" height="36" rx="12"/>
  <text class="callout-text" font-size="10" x="267" y="500" text-anchor="middle">BRAIN</text>
  <text class="callout-text" font-size="10" x="267" y="513" text-anchor="middle">FUNCTION</text>

  <rect class="callout-bubble" x="230" y="536" width="74" height="30" rx="12"/>
  <text class="callout-text" font-size="11" x="267" y="556" text-anchor="middle">GUT HEALTH</text>

  <rect class="callout-bubble" x="233" y="583" width="71" height="27" rx="12"/>
  <text class="callout-text" font-size="11" x="268" y="601" text-anchor="middle">AND MORE</text>

  <!-- front panel -->
  <text class="brand-name" x="598" y="250" font-size="60" text-anchor="middle">briskle</text>

  <rect class="headline-panel" x="478" y="284" width="226" height="152" rx="26"/>
  <text class="headline-text" x="591" y="348" font-size="40" text-anchor="middle" textLength="200" lengthAdjust="spacingAndGlyphs">SPARKLING</text>
  <text class="headline-text" x="591" y="418" font-size="64" text-anchor="middle" textLength="160" lengthAdjust="spacingAndGlyphs">WATER</text>

  <path class="ribbon" d="M501 434 L686 434 L682 450 L686 467 L501 467 L505 450 Z"/>
  <text class="callout-text callout-accent" font-size="14" x="593" y="451" text-anchor="middle">WITH REAL FRUIT</text>
  <text class="callout-text" font-size="9" x="593" y="463" text-anchor="middle">AND B VITAMINS</text>

  <path class="callout-bubble" d="M590 490 Q640 474 730 482 Q746 520 738 570 Q690 586 625 582 L596 594 L604 572 Q584 540 590 490 Z"/>
  <text class="callout-text" font-size="30" x="664" y="530" text-anchor="middle">CHERRY</text>
  <text class="callout-text" font-size="21" x="664" y="560" text-anchor="middle">FLAVOR</text>

  <g class="stat">
    <circle class="stat-badge" cx="771" cy="474" r="16"/>
    <text class="stat-number" x="771" y="479" text-anchor="middle">0</text>
    <text class="stat-word" x="771" y="486" text-anchor="middle" textLength="18" lengthAdjust="spacingAndGlyphs">CALORIES</text>
  </g>
  <g class="stat">
    <circle class="stat-badge" cx="771" cy="514" r="16"/>
    <text class="stat-number" x="771" y="519" text-anchor="middle">0</text>
    <text class="stat-word" x="771" y="526" text-anchor="middle" textLength="20" lengthAdjust="spacingAndGlyphs">SWEETENERS</text>
  </g>
  <g class="stat">
    <circle class="stat-badge" cx="771" cy="559" r="16"/>
    <text class="stat-number" x="771" y="564" text-anchor="middle">0</text>
    <text class="stat-word" x="771" y="571" text-anchor="middle" textLength="14" lengthAdjust="spacingAndGlyphs">SODIUM</text>
  </g>

  <text class="volume" x="657" y="600" text-anchor="middle">12oz (355ML)</text>

  <!-- info panel -->
  <rect class="placeholder-box" x="821" y="229" width="171" height="255"/>
  <text class="placeholder-text" x="901" y="383" text-anchor="middle">Nutrition box</text>
  <rect class="placeholder-box" x="821" y="516" width="171" height="67"/>
  <text class="placeholder-text" x="901" y="560" text-anchor="middle">Barcode</text>

  <!-- die guides -->
  <rect class="guide-line" x="146" y="133" width="874" height="493"/>
  <rect class="guide-line" x="377" y="93" width="434" height="545"/>
  <line class="guide-dash" x1="120" y1="190" x2="1067" y2="190"/>
  <line class="guide-line" x1="1041" y1="133" x2="1041" y2="626"/>
  <line class="guide-line" x1="1016" y1="118" x2="1016" y2="660" stroke-dasharray="2 3"/>
  <line class="guide-line" x1="153" y1="90" x2="153" y2="660" stroke-dasharray="2 3"/>
  <line class="guide-line" x1="146" y1="66" x2="146" y2="120"/>
  <line class="guide-line" x1="1028" y1="66" x2="1028" y2="120"/>
  <line class="guide-line" x1="1041" y1="66" x2="1041" y2="120"/>

  <text class="guide-text guide-label" x="153" y="61" text-anchor="middle">1 mm clear</text>
  <text class="guide-text guide-label" x="1028" y="61" text-anchor="middle">5 mm clear</text>
  <text class="guide-text guide-strong" x="1067" y="62">Transitional Area</text>
  <text class="guide-text guide-label-sm" x="1067" y="74">(transitions from sidewall to neck)</text>
  <line class="guide-line" x1="1084" y1="81" x2="1033" y2="137" stroke-width="1.5"/>
  <path d="M1033 137 L1034 128 L1040 132 Z" fill="var(--guide-lilac)"/>

  <text class="guide-text guide-label" x="600" y="81" text-anchor="middle">109 mm LF</text>

  <line class="guide-line" x1="96" y1="133" x2="120" y2="133"/><line class="guide-line" x1="96" y1="137" x2="120" y2="137"/>
  <text class="guide-text guide-label" x="0" y="143">2 mm clear</text>
  <line class="guide-line" x1="1058" y1="133" x2="1110" y2="133"/><line class="guide-line" x1="1058" y1="137" x2="1110" y2="137"/>
  <text class="guide-text guide-label" x="1114" y="143">2 mm clear</text>
  <line class="guide-line" x1="96" y1="618" x2="120" y2="618"/><line class="guide-line" x1="96" y1="622" x2="120" y2="622"/>
  <text class="guide-text guide-label" x="0" y="626">2 mm clear</text>
  <line class="guide-line" x1="1058" y1="618" x2="1110" y2="618"/><line class="guide-line" x1="1058" y1="622" x2="1110" y2="622"/>
  <text class="guide-text guide-label" x="1119" y="626">2 mm clear</text>

  <text class="guide-text guide-label-md" x="1063" y="362">4.875” Cut Height</text>
  <text class="guide-text guide-label-md" x="1063" y="379">123.825 MM</text>

  <line class="guide-line" x1="153" y1="656" x2="520" y2="656"/>
  <line class="guide-line" x1="655" y1="656" x2="1040" y2="656"/>
  <path d="M153 656 L160 653 L160 659 Z M1040 656 L1033 653 L1033 659 Z" fill="var(--guide-lilac)"/>
  <text class="guide-text guide-label-md" x="587" y="660" text-anchor="middle">225 MM SLIT WIDTH</text>
  <text class="guide-text guide-label-md" x="587" y="675" text-anchor="middle">8.8583”</text>

  <text class="guide-text guide-label-sm" x="169" y="700" text-anchor="middle">1mm Bkgd Bleed</text>
  <text class="guide-text guide-label-sm" x="169" y="711" text-anchor="middle">Overlap</text>
  <text class="guide-text guide-label-sm" x="960" y="682" text-anchor="middle">2mm Bkgd Only</text>
  <text class="guide-text guide-label-sm" x="960" y="694" text-anchor="middle">No Text/Art</text>
</svg>
</main>
</body>
</html>
```